Shopguidance.net

I've attached two different logo's which I both like and would like to see different designs with each logo. I'm starting a retail consulting business and blog. You can view the start of my project at shopguidance.net to get an idea of what I'm creating.
Looking for a design that says creative, strategic and community.
Updates
Hello Everyone,
Thank you for the amazing design so far.
What I Like
- double sided designs, front and back
- one side should be white or green. Customers cannot write on or make notes on an all black card
- Simple, cool, creative is best
My business card will only have the following
- Instagram
- Facebook
- Email
- Website
My new Tag line is
Think Smart. Lead Smart. Work Smart.
My title will be:
Tobin Marlowe
Retail Consultant
Please submit 1 or 2 designs with these specifications.
Thank you,
Tobin
Reason: Looking for a few more designs and have now committed the project and it is no longer refundable. Please read brief and follow specific instructions.
Looking for something simple yet creative. Something that may stand out from most cards.
Thank you,
Tobin
Thank you,
Tobin
Target Market(s)
My main target is retail managers and retail businesses that are focused on leadership and people development.
Industry/Entity Type
Retail
Look and feel
Each slider illustrates characteristics of the customer's brand and the style your logo design should communicate.

```html
<!DOCTYPE html>
<html lang="en">
<head>
<meta charset="utf-8">
<title>Shopguidance – Business Card</title>
<link rel="stylesheet" href="https://fonts.googleapis.com/css2?family=Lato:wght@400;700&family=Tinos:wght@400;700&display=swap">
<style>
  :root {
    --page: #e9e7e2;
    --ink: #1b1c1d;
    --ink-soft: #2a2c2e;
    --green: #7ccc34;
    --green-light: #a9e061;
    --green-deep: #4fa61f;
    --white: #ffffff;
  }
  * { box-sizing: border-box; margin: 0; padding: 0; }
  html, body {
    width: 1200px; height: 1023px; overflow: hidden;
    background: var(--page);
    font-family: "Lato", Arial, sans-serif;
  }
  .sheet {
    position: relative; width: 1200px; height: 1023px;
    display: flex; flex-direction: column; align-items: center; justify-content: center; gap: 60px;
  }
  .card {
    position: relative; width: 700px; height: 400px;
    border-radius: 22px; overflow: hidden;
    box-shadow: 0 10px 28px rgba(0,0,0,.22);
  }

  /* front */
  .card--front { background: linear-gradient(135deg, var(--green-light), var(--green) 60%, var(--green-deep)); }
  .front__side { position: absolute; left: 0; top: 0; bottom: 0; width: 150px; background: var(--ink); }
  .front__band {
    position: absolute; left: 150px; right: 0; top: 0; height: 120px;
    background: linear-gradient(180deg, var(--ink-soft), var(--ink));
  }
  .brand {
    position: absolute; left: 40px; top: 34px;
    display: flex; align-items: center; gap: 18px;
  }
  .brand__dot { width: 52px; height: 52px; border-radius: 50%; background: var(--green); }
  .brand__name { color: var(--white); font-weight: 700; font-size: 46px; letter-spacing: .5px; }

  .person { position: absolute; left: 180px; bottom: 70px; color: var(--white); }
  .person__name { font-family: "Tinos", "Times New Roman", serif; font-size: 27px; letter-spacing: 1px; white-space: nowrap; }
  .person__title { font-size: 17px; margin-top: 2px; }

  .divider { position: absolute; left: 470px; top: 160px; width: 2px; height: 170px; background: var(--white); }

  .contact { position: absolute; left: 492px; top: 172px; list-style: none; color: var(--white); font-size: 15px; }
  .contact li { display: flex; align-items: center; gap: 10px; margin-bottom: 16px; line-height: 1.3; white-space: nowrap; }
  .contact svg { flex: none; width: 22px; height: 22px; }

  /* back */
  .card--back { background: var(--ink); }
  .back__edge { position: absolute; top: 0; bottom: 0; width: 70px; background: var(--green); }
  .back__edge--left { left: 0; }
  .back__edge--right { right: 0; }
  .back__brand {
    position: absolute; inset: 0;
    display: flex; flex-direction: column; align-items: center; justify-content: center; gap: 22px;
  }
  .back__lockup { display: flex; align-items: center; gap: 18px; }
  .back__dot { width: 56px; height: 56px; border-radius: 50%; background: var(--green); }
  .back__name { color: var(--green); font-weight: 700; font-size: 50px; }
  .tagline { color: var(--white); font-size: 18px; letter-spacing: 1px; }
</style>
</head>
<body>
<main class="sheet">

  <section class="card card--front" aria-label="Business card front">
    <div class="front__side"></div>
    <div class="front__band"></div>
    <div class="brand">
      <span class="brand__dot"></span>
      <span class="brand__name">Shopguidance</span>
    </div>

    <div class="person">
      <p class="person__name">TOBIN MARLOWE</p>
      <p class="person__title">Retail Consultant</p>
    </div>

    <div class="divider"></div>

    <ul class="contact">
      <li>
        <svg viewBox="0 0 22 22"><circle cx="11" cy="11" r="11" fill="#fff"/><circle cx="11" cy="11" r="4" fill="#1b1c1d"/></svg>
        <span>@shopguidance</span>
      </li>
      <li>
        <svg viewBox="0 0 22 22"><circle cx="11" cy="11" r="11" fill="#fff"/><rect x="7" y="7" width="8" height="8" fill="#1b1c1d"/></svg>
        <span>/shopguidance</span>
      </li>
      <li>
        <svg viewBox="0 0 22 22"><circle cx="11" cy="11" r="11" fill="#fff"/><rect x="5.5" y="7" width="11" height="8" fill="#1b1c1d"/><path d="M5.5 7l5.5 4.5L16.5 7" stroke="#fff" stroke-width="1.2" fill="none"/></svg>
        <span>hello@shopguidance.net</span>
      </li>
      <li>
        <svg viewBox="0 0 22 22"><circle cx="11" cy="11" r="11" fill="#fff"/><circle cx="11" cy="11" r="5.5" fill="none" stroke="#1b1c1d" stroke-width="1.4"/><path d="M5.5 11h11M11 5.5c-2.5 3-2.5 8 0 11M11 5.5c2.5 3 2.5 8 0 11" stroke="#1b1c1d" stroke-width="1.1" fill="none"/></svg>
        <span>shopguidance.net</span>
      </li>
    </ul>
  </section>

  <section class="card card--back" aria-label="Business card back">
    <div class="back__edge back__edge--left"></div>
    <div class="back__edge back__edge--right"></div>
    <div class="back__brand">
      <div class="back__lockup">
        <span class="back__dot"></span>
        <span class="back__name">Shopguidance</span>
      </div>
      <p class="tagline">Think Smart. Lead Smart. Work Smart.</p>
    </div>
  </section>

</main>
</body>
</html>
```